Powerpoint template for Marlow Brook Consulting

I need a powerpoint template for my business that would also work for Google slides.
I intermittently deliver training to people and I want a nice powerpoint template, that could also work in google docs to help make production easier and more seamless for me. I also sometimes product reports and analyses that are best done in powerpoint or Google slides. I need a title page, Title and content page, section heading page and any other pages that someone normally has!

Target Market(s)

Leaders and managers in medium to large companies. I provide training and coaching services to senior staff who have got 'stuck' and want help to find their way forward.

Font styles to use
Sans Serif

Requirements
Must have
• Colours and fonts to fit with logo please.
• Must include the logo and company name.
Nice to have
• a picture for the front?

```html
<!DOCTYPE html>
<html lang="en">
<head>
<meta charset="utf-8">
<title>Marlow Brook Consulting – Presentation Template</title>
<link href="https://fonts.googleapis.com/css2?family=Open+Sans:wght@400;600;700;800&display=swap" rel="stylesheet">
<style>
:root{
  --purple:#4b2a97;
  --purple-dark:#3f2386;
  --purple-soft:#b9a8f0;
  --teal:#2fae8c;
  --teal-dark:#239877;
  --ink:#555;
  --muted:#8a8a8a;
  --stage:#8c8c8c;
  --row-a:#ececec;
  --row-b:#f5f5f5;
  --bar-light:#2f5fc4;
  --bar-dark:#1f3a8c;
}
*{margin:0;padding:0;box-sizing:border-box}
html,body{width:1200px;height:1200px;overflow:hidden}
body{background:var(--stage);font-family:"Open Sans",Arial,sans-serif;position:relative}
.pos{position:absolute}
.pos.big{width:514px;height:279px;overflow:hidden}
.pos.big .slide{transform:scale(1.849,1.86);transform-origin:0 0}
.slide{position:absolute;left:0;top:0;width:278px;height:150px;background:#fff;overflow:hidden;color:var(--ink)}
.slide.purple{background:var(--purple)}

/* header block */
.hd{position:absolute;left:14px;top:0}
.hd .line{position:absolute;left:1px;top:0;width:.6px;height:55px;background:var(--teal)}
.hd .bar{position:absolute;left:0;top:16px;width:2px;height:18px;background:var(--purple)}
.hd .sub{position:absolute;left:7px;top:17px;font-size:6.6px;color:var(--purple);white-space:nowrap;line-height:1}
.hd .ttl{position:absolute;left:7px;top:24.5px;font-size:8.6px;font-weight:700;color:var(--purple);white-space:nowrap;line-height:1}

/* brand mark */
.brand{position:absolute;right:6px;top:5px;width:34px;text-align:center}
.brand .dot{display:block;width:8px;height:8px;border-radius:50%;background:var(--teal);margin:0 auto 1.5px}
.brand span{display:block;font-size:3.3px;line-height:1.15;color:var(--purple);font-weight:600;text-transform:uppercase}

.foot{position:absolute;left:5px;bottom:2.5px;font-size:3.6px;color:var(--ink)}
.page{position:absolute;right:5px;bottom:3px;width:9px;height:9px;border-radius:50%;background:var(--teal);color:#fff;font-size:4px;font-weight:700;display:flex;align-items:center;justify-content:center}

.body{position:absolute;font-size:3.4px;line-height:1.75;color:var(--muted)}
.body p+p{margin-top:4.5px}

/* icons */
.icons{position:absolute;left:0;right:0;display:flex;justify-content:space-around;padding:0 14px}
.icon-col{width:72px;text-align:center}
.icon-col svg{width:16px;height:16px;display:block;margin:0 auto 4px}
.icon-col h4{font-size:5px;font-weight:700;margin-bottom:1px;line-height:1.2}
.icon-col p{font-size:3.6px;line-height:1.6}
.band{position:absolute;left:0;top:55px;width:278px;height:95px;background:linear-gradient(100deg,var(--teal) 0%,#35b694 50%,var(--teal) 100%)}
.band .icon-col{color:#fff}
.band .icon-col svg{fill:#fff}
.white-icons .icon-col h4{color:var(--teal)}
.white-icons .icon-col svg{fill:var(--purple)}
.white-icons .icon-col p{color:var(--muted);font-size:3px}

/* title & divider */
.vline{position:absolute;width:1.4px;background:var(--purple-soft)}
.big-title{position:absolute;color:#fff;font-weight:800;line-height:1;white-space:nowrap}
.big-sub{position:absolute;color:#fff;line-height:1;white-space:nowrap}
.title-logo{position:absolute;left:188px;top:44px;width:84px;text-align:center;color:var(--purple)}
.title-logo .dot{display:block;width:22px;height:22px;border-radius:50%;background:var(--teal);margin:0 auto 4px}
.title-logo span{display:block;font-size:6.6px;line-height:1.15;font-weight:600;text-transform:uppercase}

.photo{position:absolute}
.ph-wrist{background:linear-gradient(135deg,#14243f 0%,#2b3d63 45%,#d9dde4 60%,#1b2b4a 80%)}
.ph-hands{background:linear-gradient(120deg,#d9a274 0%,#b5562a 40%,#3a2a22 65%,#6a4630 100%)}
.ph-group{background:linear-gradient(180deg,#f1d6a8 0%,#d9a866 55%,#8c6a3e 100%)}
.ph-watch{background:linear-gradient(135deg,#6f5ad0 0%,#3d2a8c 45%,#1d1550 70%,#5a48b8 100%)}

/* table */
.tbl{position:absolute;left:8px;top:39px;width:264px;border-collapse:collapse;font-size:3.2px}
.tbl th{background:var(--teal);color:#fff;text-align:left;font-weight:700;padding:1.2px 6px;height:5px}
.tbl td{padding:0 4px;height:19.5px;color:var(--muted);line-height:1.5}
.tbl tr:nth-child(odd) td{background:var(--row-a)}
.tbl tr:nth-child(even) td{background:var(--row-b)}
.tbl td.k{width:30px;font-weight:600;color:var(--ink);text-align:center;border-right:1px solid #fff}
</style>
</head>
<body>

<!-- ============ LEFT COLUMN ============ -->

<!-- icons slide -->
<div class="pos" style="left:42px;top:26px">
  <div class="slide">
    <div class="hd"><div class="line"></div><div class="bar"></div><div class="sub">Subtitle Here</div><div class="ttl">Paragraph Title</div></div>
    <div class="brand"><i class="dot"></i><span>Marlow Brook Consulting</span></div>
    <div class="band">
      <div class="icons" style="top:9px">
        <div class="icon-col"><svg viewBox="0 0 24 24"><rect x="7" y="1" width="11" height="21" rx="2"/><rect x="9" y="4" width="7" height="14" fill="#35b694"/><path d="M3 12h5v10H5a3 3 0 0 1-2-3z"/></svg><h4>Icon Text Here</h4><p>Lorem ipsum is simply dummy text of the printing and typesetting industry. Lorem Ipsum has been the industry's standard dummy text ever since the 1500s, when an unknown printer took a galley of type and scrambled</p></div>
        <div class="icon-col"><svg viewBox="0 0 24 24"><circle cx="12" cy="5" r="3"/><circle cx="5" cy="8" r="2.3"/><circle cx="19" cy="8" r="2.3"/><path d="M7 22V13a5 5 0 0 1 10 0v9z"/><path d="M1 21v-6a4 4 0 0 1 5-3v9z"/><path d="M23 21v-6a4 4 0 0 0-5-3v9z"/></svg><h4>Icon Text Here</h4><p>Lorem ipsum is simply dummy text of the printing and typesetting industry. Lorem Ipsum has been the industry's standard dummy text ever since the 1500s, when an unknown printer took a galley of type and scrambled</p></div>
        <div class="icon-col"><svg viewBox="0 0 24 24"><rect x="2" y="14" width="3" height="9"/><rect x="7" y="11" width="3" height="12"/><rect x="12" y="12" width="3" height="11"/><rect x="17" y="8" width="3" height="15"/><path d="M2 11l6-4 5 2 8-6" stroke="#fff" stroke-width="1.2" fill="none"/></svg><h4>Icon Text Here</h4><p>Lorem ipsum is simply dummy text of the printing and typesetting industry. Lorem Ipsum has been the industry's standard dummy text ever since the 1500s, when an unknown printer took a galley of type and scrambled</p></div>
      </div>
    </div>
  </div>
</div>

<!-- title slide -->
<div class="pos" style="left:42px;top:194px">
  <div class="slide purple">
    <svg class="photo" width="278" height="150" viewBox="0 0 278 150"><polygon points="84,0 278,0 278,150 239,150" fill="#fff"/><polygon points="230,0 278,0 278,46" fill="var(--teal)"/></svg>
    <div class="title-logo"><i class="dot"></i><span>Marlow Brook Consulting</span></div>
    <div class="vline" style="left:31px;top:97px;height:17px"></div>
    <div class="big-title" style="left:39px;top:99px;font-size:8.6px">Project Title Here</div>
    <div class="big-sub" style="left:39px;top:110px;font-size:6.4px">Subtitle Here</div>
  </div>
</div>

<!-- brand left / text right -->
<div class="pos" style="left:42px;top:354px">
  <div class="slide">
    <div class="title-logo" style="left:20px;top:40px;width:100px"><i class="dot"></i><span>Marlow Brook Consulting</span></div>
    <div class="hd" style="left:124px"><div class="line" style="height:150px"></div><div class="bar" style="top:44px"></div><div class="sub" style="top:45px">Subtitle Here</div><div class="ttl" style="top:52px">Paragraph Title</div></div>
    <div class="brand"><i class="dot"></i><span>Marlow Brook Consulting</span></div>
    <div class="body" style="left:131px;top:64px;width:134px;font-size:3.2px"><p>Lorem Ipsum is simply dummy text of the printing and typesetting industry. Lorem Ipsum has been the industry's standard dummy text ever since the 1500s, when an unknown printer took a galley of type and scrambled it to make a type specimen book. It has survived not only five centuries, but also the leap into electronic typesetting, remaining essentially unchanged. It was popularised in the 1960s with the release of Letraset sheets containing Lorem Ipsum passages, and more recently with desktop publishing software like Aldus PageMaker including versions of Lorem Ipsum.</p></div>
    <div class="foot">Copyright text here</div><div class="page">01</div>
  </div>
</div>

<!-- photo left / text right -->
<div class="pos" style="left:42px;top:514px">
  <div class="slide">
    <div class="photo ph-wrist" role="img" aria-label="Photo of a businessman in a suit checking a smartwatch" style="left:0;top:0;width:106px;height:143px"></div>
    <div class="hd" style="left:124px"><div class="line" style="height:150px"></div><div class="bar" style="top:44px"></div><div class="sub" style="top:45px">Subtitle Here</div><div class="ttl" style="top:52px">Paragraph Title</div></div>
    <div class="brand"><i class="dot"></i><span>Marlow Brook Consulting</span></div>
    <div class="body" style="left:131px;top:64px;width:134px;font-size:3.2px"><p>Lorem Ipsum is simply dummy text of the printing and typesetting industry. Lorem Ipsum has been the industry's standard dummy text ever since the 1500s, when an unknown printer took a galley of type and scrambled it to make a type specimen book. It has survived not only five centuries, but also the leap into electronic typesetting, remaining essentially unchanged. It was popularised in the 1960s with the release of Letraset sheets containing Lorem Ipsum passages, and more recently with desktop publishing software like Aldus PageMaker.</p></div>
    <div class="foot">Copyright text here</div><div class="page">01</div>
  </div>
</div>

<!-- text top / photos bottom -->
<div class="pos" style="left:42px;top:687px">
  <div class="slide">
    <div class="hd"><div class="line" style="height:70px"></div><div class="bar" style="top:40px"></div><div class="sub" style="top:41px">Subtitle Here</div><div class="ttl" style="top:48.5px">Paragraph Title</div></div>
    <div class="brand"><i class="dot"></i><span>Marlow Brook Consulting</span></div>
    <div class="body" style="left:102px;top:37px;width:160px;font-size:3.2px"><p>Lorem Ipsum is simply dummy text of the printing and typesetting industry. Lorem Ipsum has been the industry's standard dummy text ever since the 1500s, when an unknown printer took a galley of type and scrambled it to make a type specimen book. It has survived not only five centuries, but also the leap into electronic a type specimen book.</p></div>
    <div class="photo ph-wrist" role="img" aria-label="Photo of a wrist wearing a smartwatch" style="left:102px;top:80px;width:47px;height:63px"></div>
    <div class="photo ph-group" role="img" aria-label="Photo of a group of friends embracing at sunset" style="left:150px;top:80px;width:128px;height:63px"></div>
    <div class="foot">Copyright text here</div><div class="page">01</div>
  </div>
</div>

<!-- table slide -->
<div class="pos" style="left:42px;top:850px">
  <div class="slide">
    <div class="hd"><div class="line" style="height:30px"></div><div class="bar" style="top:6px"></div><div class="sub" style="top:7px">Subtitle Here</div><div class="ttl" style="top:14.5px">Paragraph Title</div></div>
    <div class="brand"><i class="dot"></i><span>Marlow Brook Consulting</span></div>
    <table class="tbl">
      <tr><th style="width:30px">SECTION</th><th>MAIN TITLE HERE</th></tr>
      <tr><td class="k">ICON - 1</td><td>Liquorice chupa chups applicake apple pie cupcake brownie bear claw cake gingerbread cotton candy. Bear claw croissant apple pie. Croissant cake sweet puff oreo.</td></tr>
      <tr><td class="k">ICON - 1</td><td>Liquorice chupa chups applicake apple pie cupcake brownie bear claw cake gingerbread cotton candy. Bear claw croissant apple pie. Croissant cake sweet puff oreo.</td></tr>
      <tr><td class="k">ICON - 1</td><td>Liquorice chupa chups applicake apple pie cupcake brownie bear claw cake gingerbread cotton candy. Bear claw croissant apple pie. Croissant cake sweet puff oreo.</td></tr>
      <tr><td class="k">ICON - 1</td><td>Liquorice chupa chups applicake apple pie cupcake brownie bear claw cake gingerbread cotton candy. Bear claw croissant apple pie. Croissant cake sweet puff oreo.</td></tr>
      <tr><td class="k">ICON - 1</td><td>Liquorice chupa chups applicake apple pie cupcake brownie bear claw cake gingerbread cotton candy. Bear claw croissant apple pie. Croissant cake sweet puff oreo.</td></tr>
    </table>
    <div class="foot">Copyright text here</div><div class="page">01</div>
  </div>
</div>

<!-- mountain graph -->
<div class="pos" style="left:42px;top:1014px">
  <div class="slide">
    <div class="hd"><div class="line" style="height:30px"></div><div class="bar" style="top:6px"></div><div class="sub" style="top:7px">Subtitle Here</div><div class="ttl" style="top:14.5px">Graphs Title</div></div>
    <div class="brand"><i class="dot"></i><span>Marlow Brook Consulting</span></div>
    <svg class="photo" style="left:0;top:0" width="278" height="150" viewBox="0 0 278 150">
      <g opacity=".95">
        <polygon points="10,133 34,104 58,133" fill="#3bbf95"/>
        <polygon points="44,133 70,81 96,133" fill="#2aa37d"/>
        <polygon points="76,133 105,57 134,133" fill="#34b48c"/>
        <polygon points="116,133 141,90 166,133" fill="#1f8b68"/>
        <polygon points="146,133 175,68 204,133" fill="#3ac39a"/>
        <polygon points="188,133 211,110 234,133" fill="#2aa37d"/>
        <polygon points="216,133 245,103 274,133" fill="#48cba3"/>
      </g>
      <g fill="var(--teal)">
        <circle cx="34" cy="91" r="6"/><circle cx="70" cy="68" r="6"/><circle cx="105" cy="44" r="6"/>
        <circle cx="141" cy="77" r="6" fill="#1f6b52"/><circle cx="175" cy="57" r="6"/><circle cx="211" cy="97" r="6"/><circle cx="245" cy="90" r="6"/>
      </g>
      <g fill="#fff">
        <rect x="32" y="89.5" width="4" height="3" rx="1"/><path d="M68 66h4v4h-4z"/><path d="M103 42h4v4h-4z"/>
        <circle cx="141" cy="77" r="2"/><path d="M173 55h4v4h-4z"/><path d="M210 95h2v4h-2z"/><rect x="243" y="88" width="4" height="3"/>
      </g>
    </svg>
    <div class="foot">Copyright text here</div><div class="page">01</div>
  </div>
</div>

<!-- ============ MIDDLE COLUMN ============ -->

<!-- divider -->
<div class="pos" style="left:338px;top:26px">
  <div class="slide purple">
    <div class="vline" style="left:17px;top:63px;height:23px"></div>
    <div class="big-title" style="left:24px;top:66px;font-size:8.6px">Sectione Divider Title Here</div>
    <div class="big-sub" style="left:24px;top:77px;font-size:6.4px">Subtitle Here</div>
  </div>
</div>

<!-- text slide -->
<div class="pos" style="left:338px;top:194px">
  <div class="slide">
    <div class="hd"><div class="line"></div><div class="bar"></div><div class="sub">Subtitle Here</div><div class="ttl">Paragraph Title</div></div>
    <div class="brand"><i class="dot"></i><span>Marlow Brook Consulting</span></div>
    <div class="body" style="left:20px;top:37px;width:245px;font-size:3.3px"><p>Lorem Ipsum is simply dummy text of the printing and typesetting industry. Lorem Ipsum has been the industry's standard dummy text ever since the 1500s, when an unknown printer took a galley of type and scrambled it to make a type specimen book. It has survived not only five centuries, but also the leap into electronic typesetting, remaining essentially unchanged. It was popularised in the 1960s with the release of Letraset sheets containing Lorem Ipsum passages, and more recently with desktop publishing software like Aldus PageMaker including versions of Lorem Ipsum.</p><p>Lorem Ipsum has been the industry's standard dummy text ever since the 1500s, when an unknown printer took a galley of type and scrambled it to make a type specimen book. It has survived not only five centuries, remaining essentially unchanged.</p><p>It was popularised in the 1960s with the release of Letraset sheets containing Lorem Ipsum passages, and more recently with desktop publishing software.</p></div>
    <div class="foot">Copyright text here</div><div class="page">01</div>
  </div>
</div>

<!-- two columns -->
<div class="pos" style="left:338px;top:354px">
  <div class="slide">
    <div class="hd"><div class="line"></div><div class="bar"></div><div class="sub">Subtitle Here</div><div class="ttl">Paragraph Title</div></div>
    <div class="brand"><i class="dot"></i><span>Marlow Brook Consulting</span></div>
    <div class="body" style="left:20px;top:37px;width:118px;font-size:3.2px"><p>Lorem Ipsum is simply dummy text of the printing and typesetting industry. Lorem Ipsum has been the industry's standard dummy text ever since the 1500s, when an unknown printer took a galley of type and scrambled it to make a type specimen book. It has survived not only five centuries, but also the leap into electronic typesetting, remaining essentially unchanged. It was popularised in the 1960s with the release of Letraset sheets containing Lorem Ipsum passages, and more recently with desktop publishing software like Aldus PageMaker including versions of Lorem Ipsum.</p></div>
    <div class="body" style="left:148px;top:37px;width:118px;font-size:3.2px"><p>Lorem Ipsum is simply dummy text of the printing and typesetting industry. Lorem Ipsum has been the industry's standard dummy text ever since the 1500s, when an unknown printer took a galley of type and scrambled it to make a type specimen book. It has survived not only five centuries, but also the leap into electronic typesetting, remaining essentially unchanged. It was popularised in the 1960s with the release of Letraset sheets containing Lorem Ipsum passages, and more recently with desktop publishing software like Aldus PageMaker including versions of Lorem Ipsum.</p></div>
    <div class="foot">Copyright text here</div><div class="page">01</div>
  </div>
</div>

<!-- icons on white -->
<div class="pos" style="left:338px;top:514px">
  <div class="slide white-icons">
    <div class="hd"><div class="line"></div><div class="bar"></div><div class="sub">Subtitle Here</div><div class="ttl">Paragraph Title</div></div>
    <div class="brand"><i class="dot"></i><span>Marlow Brook Consulting</span></div>
    <div class="icons" style="top:52px">
      <div class="icon-col"><svg viewBox="0 0 24 24"><rect x="7" y="1" width="11" height="21" rx="2"/><rect x="9" y="4" width="7" height="14" fill="#fff"/><path d="M3 12h5v10H5a3 3 0 0 1-2-3z"/></svg><h4>Icon Text Here</h4><p>Lorem ipsum is simply dummy text of the printing and typesetting industry. Lorem Ipsum has been the industry's standard dummy text ever since the 1500s, when an unknown printer took a galley of type and scrambled</p></div>
      <div class="icon-col"><svg viewBox="0 0 24 24" style="fill:var(--teal)"><circle cx="12" cy="5" r="3"/><circle cx="5" cy="8" r="2.3"/><circle cx="19" cy="8" r="2.3"/><path d="M7 22V13a5 5 0 0 1 10 0v9z"/><path d="M1 21v-6a4 4 0 0 1 5-3v9z"/><path d="M23 21v-6a4 4 0 0 0-5-3v9z"/></svg><h4>Icon Text Here</h4><p>Lorem ipsum is simply dummy text of the printing and typesetting industry. Lorem Ipsum has been the industry's standard dummy text ever since the 1500s, when an unknown printer took a galley of type and scrambled</p></div>
      <div class="icon-col"><svg viewBox="0 0 24 24"><rect x="2" y="14" width="3" height="9"/><rect x="7" y="11" width="3" height="12"/><rect x="12" y="12" width="3" height="11"/><rect x="17" y="8" width="3" height="15"/><path d="M2 11l6-4 5 2 8-6" stroke="var(--purple)" stroke-width="1.2" fill="none"/></svg><h4>Icon Text Here</h4><p>Lorem ipsum is simply dummy text of the printing and typesetting industry. Lorem Ipsum has been the industry's standard dummy text ever since the 1500s, when an unknown printer took a galley of type and scrambled</p></div>
    </div>
    <div class="foot">Copyright text here</div><div class="page">01</div>
  </div>
</div>

<!-- purple text / photo right -->
<div class="pos" style="left:338px;top:687px">
  <div class="slide">
    <div class="photo" style="left:0;top:0;width:121px;height:143px;background:var(--purple)"></div>
    <div class="photo ph-hands" role="img" aria-label="Photo of a hand touching a smartwatch on a wrist" style="left:121px;top:0;width:157px;height:143px"></div>
    <div class="hd"><div class="line" style="background:var(--purple-soft);height:50px"></div><div class="bar" style="background:#fff;top:27px"></div><div class="sub" style="top:28px;color:#fff">Subtitle Here</div><div class="ttl" style="top:35.5px;color:#fff">Paragraph Title</div></div>
    <div class="body" style="left:20px;top:45px;width:96px;font-size:3.3px;color:#fff"><p>Lorem Ipsum is simply dummy text of the printing and typesetting industry. Lorem Ipsum has been the industry's standard dummy text ever since the 1500s, when an unknown printer took a galley of type and scrambled it to make a type specimen book. It has survived not only five centuries, but also the leap into electronic a type specimen book.</p></div>
    <div class="foot">Copyright text here</div><div class="page">01</div>
  </div>
</div>

<!-- purple photo with overlay box -->
<div class="pos" style="left:338px;top:850px">
  <div class="slide">
    <div class="photo ph-watch" role="img" aria-label="Purple-tinted photo of a hand holding a smartwatch" style="left:0;top:0;width:278px;height:143px"></div>
    <div class="photo" style="left:155px;top:0;width:97px;height:104px;background:var(--purple)"></div>
    <div class="hd" style="left:160px"><div class="bar" style="background:#fff;top:9px;height:14px"></div><div class="sub" style="left:3px;top:10px;color:#fff">Subtitle Here</div><div class="ttl" style="left:3px;top:17.5px;color:#fff">Paragraph Title</div></div>
    <div class="body" style="left:163px;top:28px;width:84px;font-size:3.1px;color:#fff"><p>Lorem Ipsum is simply dummy text of the printing and typesetting industry. Lorem Ipsum has been the industry's standard dummy text ever since the 1500s, when an unknown printer took a galley of type and scrambled it to make a type specimen book. It has survived not only five centuries, but also the leap into electronic a type specimen book.</p></div>
    <div class="foot">Copyright text here</div><div class="page">01</div>
  </div>
</div>

<!-- bar graphs -->
<div class="pos" style="left:338px;top:1014px">
  <div class="slide">
    <div class="hd"><div class="line" style="height:30px"></div><div class="bar" style="top:6px"></div><div class="sub" style="top:7px">Subtitle Here</div><div class="ttl" style="top:14.5px">Graphs Title</div></div>
    <div class="brand"><i class="dot"></i><span>Marlow Brook Consulting</span></div>
    <svg class="photo" style="left:0;top:0" width="278" height="150" viewBox="0 0 278 150" font-family="Open Sans, sans-serif" font-size="3" fill="#999">
      <g stroke="#ccc" stroke-width=".4">
        <line x1="30" y1="43" x2="30" y2="129"/><line x1="30" y1="129" x2="90" y2="129"/>
        <line x1="118" y1="43" x2="118" y2="129"/><line x1="118" y1="129" x2="178" y2="129"/>
        <line x1="206" y1="43" x2="206" y2="129"/><line x1="206" y1="129" x2="266" y2="129"/>
      </g>
      <g>
        <text x="25" y="45">5</text><text x="25" y="63">4</text><text x="25" y="80">3</text><text x="25" y="97">2</text><text x="25" y="114">1</text>
        <text x="113" y="45">5</text><text x="113" y="63">4</text><text x="113" y="80">3</text><text x="113" y="97">2</text><text x="113" y="114">1</text>
        <text x="201" y="45">5</text><text x="201" y="63">4</text><text x="201" y="80">3</text><text x="201" y="97">2</text><text x="201" y="114">1</text>
      </g>
      <rect x="33" y="112" width="13" height="17" fill="var(--bar-light)"/>
      <rect x="46" y="103" width="13" height="26" fill="var(--bar-dark)"/>
      <rect x="59" y="95" width="13" height="34" fill="var(--bar-light)"/>
      <rect x="72" y="78" width="13" height="51" fill="var(--bar-dark)"/>
      <rect x="121" y="125" width="13" height="4" fill="var(--bar-light)"/>
      <rect x="134" y="108" width="13" height="21" fill="var(--bar-dark)"/>
      <rect x="147" y="111" width="13" height="18" fill="var(--bar-light)"/>
      <rect x="160" y="103" width="13" height="26" fill="var(--bar-dark)"/>
      <rect x="209" y="46" width="13" height="83" fill="var(--bar-light)"/>
      <rect x="222" y="95" width="13" height="34" fill="var(--bar-dark)"/>
      <rect x="235" y="69" width="13" height="60" fill="var(--bar-dark)"/>
      <rect x="248" y="95" width="13" height="34" fill="var(--bar-light)"/>
    </svg>
    <div class="foot">Copyright text here</div><div class="page">01</div>
  </div>
</div>

<!-- ============ RIGHT COLUMN (large) ============ -->

<div class="pos big" style="left:634px;top:27px">
  <div class="slide">
    <div class="hd"><div class="line"></div><div class="bar"></div><div class="sub">Subtitle Here</div><div class="ttl">Paragraph Title</div></div>
    <div class="brand"><i class="dot"></i><span>Marlow Brook Consulting</span></div>
    <div class="band">
      <div class="icons" style="top:9px">
        <div class="icon-col"><svg viewBox="0 0 24 24"><rect x="7" y="1" width="11" height="21" rx="2"/><rect x="9" y="4" width="7" height="14" fill="#35b694"/><path d="M3 12h5v10H5a3 3 0 0 1-2-3z"/></svg><h4>Icon Text Here</h4><p>Lorem Ipsum is simply dummy text of the printing and typesetting industry. Lorem Ipsum has been the industry's standard dummy text ever since the 1500s, when an unknown printer took a galley of type and scrambled</p></div>
        <div class="icon-col"><svg viewBox="0 0 24 24"><circle cx="12" cy="5" r="3"/><circle cx="5" cy="8" r="2.3"/><circle cx="19" cy="8" r="2.3"/><path d="M7 22V13a5 5 0 0 1 10 0v9z"/><path d="M1 21v-6a4 4 0 0 1 5-3v9z"/><path d="M23 21v-6a4 4 0 0 0-5-3v9z"/></svg><h4>Icon Text Here</h4><p>Lorem Ipsum is simply dummy text of the printing and typesetting industry. Lorem Ipsum has been the industry's standard dummy text ever since the 1500s, when an unknown printer took a galley of type and scrambled</p></div>
        <div class="icon-col"><svg viewBox="0 0 24 24"><rect x="2" y="14" width="3" height="9"/><rect x="7" y="11" width="3" height="12"/><rect x="12" y="12" width="3" height="11"/><rect x="17" y="8" width="3" height="15"/><path d="M2 11l6-4 5 2 8-6" stroke="#fff" stroke-width="1.2" fill="none"/></svg><h4>Icon Text Here</h4><p>Lorem Ipsum is simply dummy text of the printing and typesetting industry. Lorem Ipsum has been the industry's standard dummy text ever since the 1500s, when an unknown printer took a galley of type and scrambled</p></div>
      </div>
    </div>
  </div>
</div>

<div class="pos big" style="left:634px;top:312px">
  <div class="slide purple">
    <svg class="photo" width="278" height="150" viewBox="0 0 278 150"><polygon points="84,0 278,0 278,150 239,150" fill="#fff"/><polygon points="230,0 278,0 278,46" fill="var(--teal)"/></svg>
    <div class="title-logo"><i class="dot"></i><span>Marlow Brook Consulting</span></div>
    <div class="vline" style="left:27px;top:98px;height:18px"></div>
    <div class="big-title" style="left:32px;top:99px;font-size:9.4px">Project Title Here</div>
    <div class="big-sub" style="left:32px;top:111px;font-size:6.8px">Subtitle Here</div>
  </div>
</div>

<div class="pos big" style="left:634px;top:599px">
  <div class="slide purple">
    <div class="vline" style="left:17px;top:66px;height:25px"></div>
    <div class="big-title" style="left:24px;top:68px;font-size:9.4px">Sectione Divider Title Here</div>
    <div class="big-sub" style="left:24px;top:80px;font-size:6.8px">Subtitle Here</div>
  </div>
</div>

<div class="pos big" style="left:634px;top:892px">
  <div class="slide">
    <div class="hd"><div class="line"></div><div class="bar"></div><div class="sub">Subtitle Here</div><div class="ttl">Paragraph Title</div></div>
    <div class="brand"><i class="dot"></i><span>Marlow Brook Consulting</span></div>
    <div class="body" style="left:21px;top:37px;width:246px;font-size:4.2px;line-height:1.75"><p>Lorem Ipsum is simply dummy text of the printing and typesetting industry. Lorem Ipsum has been the industry's standard dummy text ever since the 1500s, when an unknown printer took a galley of type and scrambled it to make a type specimen book. It has survived not only five centuries, but also the leap into electronic typesetting, remaining essentially unchanged. It was popularised in the 1960s with the release of Letraset sheets containing Lorem Ipsum passages, and more recently with desktop publishing software like Aldus PageMaker including versions of Lorem Ipsum. Lorem Ipsum is simply dummy text of the printing and typesetting industry.</p><p>Lorem Ipsum has been the industry's standard dummy text ever since the 1500s, when an unknown printer took a galley of type and scrambled it to make a type specimen book. It has survived not only five centuries, but also the leap into electronic typesetting, remaining essentially unchanged.</p><p>It was popularised in the 1960s with the release of Letraset sheets containing Lorem Ipsum passages, and more recently with desktop publishing software like Aldus PageMaker including versions of Lorem Ipsum.</p></div>
    <div class="foot">Copyright text here</div><div class="page">01</div>
  </div>
</div>

</body>
</html>
```